Maple Hollow Farm Business Card

Farm selling Nigerian Dwarf Goats, Bison, chickens, and miniature donkeys. Additionally we sell goats milk, goats milk soap and goat cheese, bison meat, bison heads, and bison skins, and chicken eggs.
Address 4125 Larkspur Road
Cedar Springs, KY 40999
Phone number 555-283-1947
Website: MapleHollowFarm@examplemail.com
I will upload my farm logo, cheese label, and soap label to give you ideas of my theme.
I want a really catchy card that people will remember.

```html
<!DOCTYPE html>
<html lang="en">
<head>
<meta charset="utf-8">
<title>Maple Hollow Farm Business Card</title>
<link href="https://fonts.googleapis.com/css2?family=Cormorant+Garamond:ital,wght@1,500;1,600&display=swap" rel="stylesheet">
<style>
  :root {
    --backdrop: #b9b5b3;
    --card-edge: #fbf8c6;
    --band-gold: #f2b520;
    --band-gold-deep: #e0a012;
    --panel-brown: #2c231b;
    --text-gold: #d9a21f;
    --text-cream: #f4efe2;
    --stroke-gold: #e9b424;
    --ring-rope: #a8632a;
  }
  * { margin: 0; padding: 0; box-sizing: border-box; }
  html, body {
    width: 1200px; height: 800px; overflow: hidden;
    background: var(--backdrop);
  }
  .sheet {
    width: 1200px; height: 800px;
    display: flex; align-items: center; justify-content: center; gap: 60px;
  }
  .card {
    width: 540px; height: 320px;
    background: var(--card-edge);
    padding: 9px;
    display: flex; gap: 8px;
    box-shadow: 0 10px 24px rgba(0,0,0,0.25);
    font-family: "Cormorant Garamond", Georgia, serif;
    font-style: italic;
  }
  .band {
    background: linear-gradient(160deg, var(--band-gold-deep), var(--band-gold));
  }
  .band--left { width: 115px; }
  .band--right { width: 100px; }
  .panel {
    flex: 1;
    background: var(--panel-brown);
    padding: 18px 16px;
    color: var(--text-cream);
    position: relative;
  }

  /* contact side */
  .farm-name {
    color: var(--text-gold);
    font-size: 28px; font-weight: 500;
    text-align: center;
    line-height: 1.1;
  }
  .brush-stroke {
    display: block; height: 7px; margin: 14px 6px;
    background: var(--stroke-gold);
    border-radius: 4px;
  }
  .address {
    font-size: 19px; font-weight: 600; text-align: center; line-height: 1.25;
  }
  .contact {
    position: absolute; left: 16px; right: 12px; bottom: 18px;
    font-size: 14px; font-weight: 500; line-height: 1.4;
    white-space: nowrap;
  }

  /* brand side */
  .panel--brand {
    display: flex; align-items: center; justify-content: center;
  }
  .brand-mark {
    display: flex; flex-direction: column; align-items: center; gap: 12px;
  }
  .brand-art {
    width: 150px; height: 150px; border-radius: 50%;
    border: 5px solid var(--ring-rope);
    background: radial-gradient(circle, #6b5220 0%, var(--panel-brown) 75%);
  }
  .brand-name {
    color: var(--text-gold);
    font-size: 34px; font-weight: 600;
    letter-spacing: 1px;
  }
</style>
</head>
<body>
  <main class="sheet">
    <section class="card card--contact">
      <div class="band band--left"></div>
      <div class="panel">
        <h1 class="farm-name">Maple Hollow Farm</h1>
        <span class="brush-stroke"></span>
        <p class="address">4125 Larkspur Road<br>Cedar Springs, KY 40999</p>
        <span class="brush-stroke"></span>
        <p class="contact">Phone: 555-283-1947<br>Email: MapleHollowFarm@examplemail.com</p>
      </div>
      <div class="band band--right"></div>
    </section>

    <section class="card card--brand">
      <div class="band band--left"></div>
      <div class="panel panel--brand">
        <div class="brand-mark">
          <div class="brand-art" role="img" aria-label="Round farm artwork area"></div>
          <p class="brand-name">Maple Hollow</p>
        </div>
      </div>
      <div class="band band--right"></div>
    </section>
  </main>
</body>
</html>
```